Travel Business Card

Hello. I am an award-winning travel advisor in Sydney, Australia seeking new business cards reflecting a unique style. Words to describe the design I'm seeking - Contemporary, Artsy, Vibrant, Soulful, Journey.

I loved this'Absolut' design and have created a few concepts to guide you for the back of the bus card. Feel free to use your own imagination...
maybe use elements of a Venetian mask or City (Icon), Cruise Ship, Sunshine, Beach/ Beach Hut, Buddha (Spiritual), Lotus or Palm Tree (Nature), Magic Carpet (Middle East), Whale or Waves, or enhance the pencil sketch I did...

Remember. The design should look high-end and fashionable.

Looking forward to hearing from you.
My email is corinne@brightmeridian.example.

Many thanks.

Industry/Entity Type

Travel

```html
<!DOCTYPE html>
<html lang="en">
<head>
<meta charset="utf-8">
<title>Corinne Halden – Travel Advisor Business Card</title>
<link href="https://fonts.googleapis.com/css2?family=Open+Sans:wght@400;700&family=Raleway:wght@600&display=swap" rel="stylesheet">
<style>
  :root {
    --backdrop: #a7cfcd;
    --card: #f6ebe8;
    --ink: #6b5c5e;
    --sky-top: #f3dfd9;
    --sky-low: #efe3de;
    --hill: #b3dcd3;
    --peak: #d8c2b4;
    --peak-pink: #ec9fb8;
  }
  * { margin: 0; padding: 0; box-sizing: border-box; }
  html, body { width: 1200px; height: 1000px; overflow: hidden; }
  body { background: var(--backdrop); position: relative; font-family: "Open Sans", Arial, sans-serif; color: var(--ink); }

  .card { position: absolute; width: 285px; height: 500px; background: var(--card); }
  .card--front { left: 268px; top: 252px; }
  .card--back { left: 650px; top: 248px; overflow: hidden; }

  .line { position: absolute; left: 0; right: 0; height: 18px; line-height: 18px; text-align: center; font-size: 13px; white-space: nowrap; }
  .line--bold { font-weight: 700; }
  .name { font-family: "Raleway", "Open Sans", sans-serif; font-weight: 600; font-size: 23px; letter-spacing: 0.5px; height: 30px; line-height: 30px; }

  .divider { position: absolute; left: 39px; width: 202px; top: 152px; border-top: 2px dotted var(--ink); }
  .divider-stem { position: absolute; left: 141px; top: 152px; height: 34px; border-left: 2px dotted var(--ink); }
  .col { position: absolute; width: 120px; text-align: center; font-size: 13px; font-weight: 700; line-height: 18px; }
  .col--mobile { left: 22px; }
  .col--fax { left: 144px; }
  .short-dots { position: absolute; left: 124px; width: 30px; top: 342px; border-top: 2px dotted var(--ink); }

  .illustration { position: absolute; inset: 0; background:
      linear-gradient(180deg, var(--sky-top) 0%, var(--sky-low) 50%, var(--hill) 62%, var(--peak-pink) 75%, var(--peak) 88%, var(--card) 100%); }
</style>
</head>
<body>
  <section class="card card--front" aria-label="Business card front">
    <h1 class="line name" style="top:44px">CORINNE HALDEN</h1>
    <p class="line" style="top:82px">Travel Advisor</p>
    <p class="line" style="top:98px">LIC. NO. 4TR20817</p>
    <p class="line" style="top:115px">ABN. 00 000 000 000</p>

    <div class="divider"></div>
    <div class="divider-stem"></div>
    <div class="col col--mobile" style="top:173px">M<br><span style="display:block;margin-top:4px">0400 000 000</span></div>
    <div class="col col--fax" style="top:173px">F<br><span style="display:block;margin-top:4px">02 0000 0000</span></div>

    <p class="line line--bold" style="top:217px">TRAVEL@CORINNEHALDEN.EXAMPLE</p>
    <p class="line" style="top:260px">A. PO BOX XXX,</p>
    <p class="line" style="top:282px">MARLOW RIDGE, NSW 2000</p>
    <p class="line line--bold" style="top:304px">WWW. CORINNEHALDEN.EXAMPLE</p>

    <div class="short-dots"></div>

    <p class="line" style="top:359px">Over 16 years experience</p>
    <p class="line" style="top:376px">Leisure &amp; Corporate</p>
    <p class="line line--bold" style="top:392px">Australian Cruise Consultant</p>
    <p class="line line--bold" style="top:409px">of the year</p>
    <p class="line" style="top:426px">Regional cruise guild</p>
    <p class="line" style="top:443px">australasia, 2008</p>
  </section>

  <section class="card card--back" aria-label="Business card back">
    <div class="illustration" role="img" aria-label="Illustration of a rocket launching over pastel speckled mountains and teal hills under a crescent moon and small clouds"></div>
  </section>
</body>
</html>
```